Influencer agency website

K-Brightline, Influencer Marketing Agency. A creative space where influencers and brands meet. We represent ideas and collaborations which bring marketing success to companies and brands.
Influencer types: Nano, Micro, Macro
Brand Types: Fashion, Beauty, Luxury Goods, Gaming, Sports, Home & Living, Travel, Lifestyle, Automotive

```html
<!DOCTYPE html>
<html lang="en">
<head>
<meta charset="utf-8">
<title>K-Brightline – Influencer Marketing Agency</title>
<link href="https://fonts.googleapis.com/css2?family=Marcellus&family=Poppins:wght@400;500;600&display=swap" rel="stylesheet">
<style>
:root{
  --peach:#f5d9c7;
  --salmon:#eaa68b;
  --ink:#121214;
  --dark-btn:#232327;
  --yellow:#fdc441;
  --text:#6e5a52;
  --muted:#8a7f7a;
  --heading:#1d1d1f;
  --white:#ffffff;
  --blush:#f8ece6;
  --cream:#faf8f3;
}
*{margin:0;padding:0;box-sizing:border-box}
html,body{width:908px;height:1200px;overflow:hidden}
body{position:relative;background:var(--white);font-family:'Poppins',sans-serif;color:var(--heading)}
.abs{position:absolute}

.top-strip{left:0;top:0;width:908px;height:23px;background:var(--peach)}
.social-box{left:684px;top:0;width:99px;height:23px;background:var(--ink);display:flex;align-items:center;justify-content:space-evenly;padding:0 8px}
.social-dot{width:6px;height:6px;border-radius:50%;background:var(--white)}

.nav-bar{left:0;top:23px;width:908px;height:50px;background:var(--ink)}
.brand{left:76px;top:40px;font-family:'Marcellus',serif;font-size:12px;color:var(--white);letter-spacing:.5px}
.nav-link{top:42px;font-size:9px;color:var(--white)}
.btn{display:flex;align-items:center;justify-content:center;border-radius:20px;font-size:7.5px;font-weight:600;text-transform:uppercase}
.btn-yellow{background:var(--yellow);color:var(--ink)}
.btn-dark{background:var(--dark-btn);color:var(--yellow)}

.hero{left:0;top:73px;width:908px;height:433px;background:radial-gradient(ellipse 420px 300px at 640px 430px,var(--salmon),var(--peach) 100%)}
.hero-title{left:76px;top:144px;font-family:'Marcellus',serif;font-size:37px;line-height:50px;color:var(--heading);font-weight:400}
.highlight{background:var(--ink);color:var(--white);padding:0 6px 2px 5px}
.hero-copy{left:76px;top:299px;width:330px;font-size:9.4px;line-height:16px;color:var(--text)}
.hero-person{left:479px;top:92px;width:267px;height:414px;border-radius:130px 130px 0 0;background:linear-gradient(180deg,#d9a78a 0%,#e07557 55%,#d9603f 100%)}
.doodle{border-radius:12px;background:rgba(60,40,30,.08)}
.stat-circle{left:697px;top:353px;width:92px;height:92px;border-radius:50%;background:var(--yellow)}
.stat-num{left:726px;top:376px;font-size:22px;font-weight:500;color:var(--ink)}
.stat-num sup{font-size:11px;margin-left:3px}
.stat-label{left:725px;top:403px;font-size:9.5px;color:var(--ink)}

.about-photo{left:0;top:546px;width:451px;height:312px;background:linear-gradient(135deg,#b9c6cf 0%,#cdb79a 55%,#8a6c52 100%)}
.side-panel{left:833px;top:546px;width:75px;height:311px;background:var(--cream)}
.eyebrow{font-size:7.5px;font-weight:600;text-transform:uppercase;color:#5b4a42}
.section-title{font-family:'Marcellus',serif;font-size:25px;color:var(--heading);font-weight:400}
.section-copy{font-size:9.4px;line-height:16px;color:var(--muted)}
.feature-icon{width:22px;height:22px;border-radius:50%;display:flex;align-items:center;justify-content:center}
.icon-yellow{background:var(--yellow)}
.icon-dark{background:var(--ink)}
.feature-title{font-size:11.5px;font-weight:500;color:var(--heading)}
.feature-copy{font-size:9.2px;line-height:14px;color:var(--muted)}

.why{left:0;top:901px;width:908px;height:299px;background:var(--blush)}
.team-photo{left:452px;top:938px;width:381px;height:214px;background:linear-gradient(135deg,#a9a08c 0%,#cfd7e4 50%,#6f7f98 100%)}
</style>
</head>
<body>
<div class="abs top-strip"></div>
<div class="abs social-box" aria-label="Social links">
  <span class="social-dot"></span><span class="social-dot"></span><span class="social-dot"></span><span class="social-dot"></span>
</div>

<header>
  <div class="abs nav-bar"></div>
  <div class="abs brand">K-Brightline</div>
  <nav>
    <span class="abs nav-link" style="left:164px">Home</span>
    <span class="abs nav-link" style="left:216px">About</span>
    <span class="abs nav-link" style="left:267px">Influencers</span>
    <span class="abs nav-link" style="left:343px">Page</span>
    <span class="abs nav-link" style="left:391px">Testimonial</span>
    <span class="abs nav-link" style="left:469px">Blog</span>
    <span class="abs nav-link" style="left:513px">Contact</span>
  </nav>
  <a class="abs btn btn-yellow" style="left:687px;top:34px;width:93px;height:27px">Get Stated</a>
</header>

<section>
  <div class="abs hero"></div>
  <h1 class="abs hero-title">Boost business<br>with <span class="highlight">influencer</span><br>marketing</h1>
  <p class="abs hero-copy">Lorem ipsum dolor sit amet, consectetur adipiscing elit. In semper vestibulum elementum. Vestibulum ante ipsum primis in faucibus orci luctus et ultrices posuere cubilia curae;</p>
  <a class="abs btn btn-dark" style="left:76px;top:373px;width:110px;height:32px">Get Stated</a>
  <div class="abs doodle" style="left:426px;top:160px;width:83px;height:58px" role="img" aria-label="Hand-drawn speech bubble with heart and +1000 likes"></div>
  <div class="abs hero-person" role="img" aria-label="Smiling influencer woman in a coral dotted kurta pointing up"></div>
  <div class="abs doodle" style="left:740px;top:198px;width:66px;height:80px" role="img" aria-label="Hand-drawn paper plane with dashed loop"></div>
  <div class="abs stat-circle"></div>
  <div class="abs stat-num">5,420<sup>+</sup></div>
  <div class="abs stat-label">Popular Influencer</div>
</section>

<section>
  <div class="abs about-photo" role="img" aria-label="Businesswoman working at a laptop with colleagues talking behind her"></div>
  <div class="abs side-panel"></div>
  <div class="abs eyebrow" style="left:493px;top:545px">About</div>
  <h2 class="abs section-title" style="left:493px;top:559px">Get To Know Us</h2>
  <p class="abs section-copy" style="left:494px;top:596px;width:320px">Lorem ipsum dolor sit amet, consectetur adipiscing elit. In semper vestib ulum elementum. Vestibulum ante ipsum primis in faucibus .</p>

  <div class="abs feature-icon icon-yellow" style="left:495px;top:650px"><svg width="12" height="12" viewBox="0 0 12 12"><path d="M1 2h7v5H4l-2 2V7H1z" fill="#121214"/><path d="M9 4h2v5h-1v2l-2-2H5V8h4z" fill="#121214"/></svg></div>
  <div class="abs feature-title" style="left:525px;top:653px">Communication</div>
  <p class="abs feature-copy" style="left:525px;top:669px;width:300px">Lorem ipsum dolor sit amet, consectetur adipiscing elit, sed do eiusmod tempor incididunt.</p>

  <div class="abs feature-icon icon-yellow" style="left:495px;top:703px"><svg width="12" height="12" viewBox="0 0 12 12"><circle cx="6" cy="5" r="3.5" fill="#121214"/><rect x="4.5" y="8.5" width="3" height="2" fill="#121214"/></svg></div>
  <div class="abs feature-title" style="left:525px;top:706px">Creativity and Problem-Solving</div>
  <p class="abs feature-copy" style="left:525px;top:722px;width:300px">Lorem ipsum dolor sit amet, consectetur adipiscing elit, sed do eiusmod tempor incididunt.</p>

  <div class="abs feature-icon icon-yellow" style="left:495px;top:756px"><svg width="12" height="12" viewBox="0 0 12 12"><circle cx="6" cy="6" r="5.5" fill="#121214"/><rect x="5.2" y="2.5" width="1.6" height="4.5" fill="#fdc441"/><circle cx="6" cy="9" r="0.9" fill="#fdc441"/></svg></div>
  <div class="abs feature-title" style="left:525px;top:759px">Attention to Detail</div>
  <p class="abs feature-copy" style="left:525px;top:775px;width:300px">Lorem ipsum dolor sit amet, consectetur adipiscing elit, sed do eiusmod tempor incididunt.</p>

  <a class="abs btn btn-dark" style="left:493px;top:824px;width:111px;height:32px">Get Stated</a>
</section>

<section>
  <div class="abs why"></div>
  <div class="abs eyebrow" style="left:76px;top:931px">Why Choose Us</div>
  <h2 class="abs section-title" style="left:76px;top:947px">We Make Every Content Count</h2>
  <p class="abs section-copy" style="left:77px;top:984px;width:340px">Lorem ipsum dolor sit amet, consectetur adipiscing elit. In semper vestib ulum elementum. Vestibulum ante ipsum primis in faucibus .</p>

  <div class="abs feature-icon icon-dark" style="left:77px;top:1039px"><svg width="12" height="12" viewBox="0 0 12 12"><path d="M1 4l2.5 2L6 2l2.5 4L11 4v6H1z" fill="#fdc441"/></svg></div>
  <div class="abs feature-title" style="left:107px;top:1041px">Years Experience</div>
  <p class="abs feature-copy" style="left:107px;top:1056px;width:320px">consectetur adipiscing elit, sed do eiusmod tempor incididunt.</p>

  <div class="abs feature-icon icon-dark" style="left:77px;top:1078px"><svg width="12" height="12" viewBox="0 0 12 12"><circle cx="6" cy="3" r="2" fill="#fdc441"/><circle cx="2.5" cy="9" r="1.8" fill="#fdc441"/><circle cx="9.5" cy="9" r="1.8" fill="#fdc441"/><path d="M6 5v2M6 7L3 8M6 7l3 1" stroke="#fdc441" stroke-width="1"/></svg></div>
  <div class="abs feature-title" style="left:107px;top:1080px">Professional Team</div>
  <p class="abs feature-copy" style="left:107px;top:1095px;width:320px">Morbi porta, purus id porta molestie, magna ante gravida risus.</p>

  <div class="abs feature-icon icon-dark" style="left:77px;top:1117px"><svg width="12" height="12" viewBox="0 0 12 12"><path d="M6 1l4.5 1.8V6c0 2.6-2 4.3-4.5 5-2.5-.7-4.5-2.4-4.5-5V2.8z" fill="#fdc441"/><circle cx="6" cy="6" r="1.8" fill="#121214"/></svg></div>
  <div class="abs feature-title" style="left:107px;top:1119px">Guaranteed Profit</div>
  <p class="abs feature-copy" style="left:107px;top:1134px;width:320px">Sed do eiusmod tempor incididunt purus id porta molestie.</p>

  <div class="abs team-photo" role="img" aria-label="Smiling team of colleagues gathered around laptops"></div>
</section>
</body>
</html>
```